Outdoor mass notification company needing business card design.

Our company name is Harborline Signal Systems Inc located in Amory Mississippi and we sell and maintain "Corvath" Mass Notification Sirens in the US. Outdoor sirens notify people of certain severe dangers such as tornados, severe thunderstorms, flooding, hurricanes and tsunamis. We also serve the oil and gas refining industries to warn of Chemical releases, fires, and lightning alerts.

Contact Information for Business Card

Name, title, cell number, email address

Requirements
Nice to have
• The Corvath logo and also the Tallbrook logo.

```html
<!DOCTYPE html>
<html lang="en">
<head>
<meta charset="utf-8">
<title>Harborline Signal Systems – Business Card</title>
<link href="https://fonts.googleapis.com/css2?family=Roboto+Slab:wght@400;700&display=swap" rel="stylesheet">
<style>
  :root {
    --backdrop: #d3d4d6;
    --card: #ffffff;
    --navy: #2f4e6e;
    --ink: #555555;
    --siren-dark: #1e1e1e;
    --siren-mid: #4a4a4a;
  }
  * { margin: 0; padding: 0; box-sizing: border-box; }
  html, body {
    width: 900px; height: 1200px; overflow: hidden;
    background: var(--backdrop);
    font-family: "Roboto Slab", serif;
  }
  .card {
    position: absolute;
    width: 633px; height: 364px;
    background: var(--card);
  }
  .card--front { left: 133px; top: 210px; }
  .card--back { left: 134px; top: 624px; }

  .wordmark {
    position: absolute;
    color: var(--navy);
    font-weight: 700;
    text-align: right;
    line-height: 1;
    white-space: nowrap;
  }
  .card--front .wordmark { right: 118px; top: 148px; }
  .card--front .wordmark__top { font-size: 50px; }
  .card--front .wordmark__bottom { font-size: 36px; margin-top: 6px; }

  .card--back .wordmark { left: 46px; top: 164px; width: 232px; }
  .card--back .wordmark__top { font-size: 32px; }
  .card--back .wordmark__bottom { font-size: 23px; margin-top: 4px; }

  .siren-photo {
    position: absolute;
    left: 297px; top: 122px; width: 38px; height: 124px;
    background: linear-gradient(to bottom, var(--siren-dark) 0%, var(--siren-mid) 50%, var(--siren-dark) 75%, #2a2a2a 100%);
    border-radius: 3px;
  }

  .contact-block { position: absolute; left: 353px; top: 118px; }
  .contact-name {
    color: var(--navy); font-weight: 700; font-size: 24px; letter-spacing: 0.5px;
    line-height: 1;
  }
  .contact-title { color: var(--ink); font-size: 16px; margin-top: 6px; letter-spacing: 0.5px; }
  .contact-list { list-style: none; margin-top: 12px; }
  .contact-list li {
    display: flex; align-items: center; gap: 7px;
    color: var(--ink); font-size: 14.5px; letter-spacing: 1.2px;
    height: 23px;
  }
  .contact-list svg { width: 14px; height: 14px; fill: var(--navy); flex: none; }

  .address {
    position: absolute; left: 0; right: 0; top: 282px;
    text-align: center; color: var(--ink); font-size: 16.5px; letter-spacing: 0.4px;
  }
  .address svg { display: block; margin: 0 auto 8px; width: 12px; height: 16px; fill: var(--navy); }
</style>
</head>
<body>

<section class="card card--front">
  <div class="wordmark">
    <div class="wordmark__top">HARBORLINE</div>
    <div class="wordmark__bottom">SIGNAL SYSTEMS</div>
  </div>
</section>

<section class="card card--back">
  <div class="wordmark">
    <div class="wordmark__top">HARBORLINE</div>
    <div class="wordmark__bottom">SIGNAL SYSTEMS</div>
  </div>

  <div class="siren-photo" role="img" aria-label="Photo of an outdoor mass notification siren on a pole"></div>

  <div class="contact-block">
    <div class="contact-name">DANA WHITCOMBE</div>
    <div class="contact-title">Owner</div>
    <ul class="contact-list">
      <li>
        <svg viewBox="0 0 24 24" aria-hidden="true"><path d="M6.6 10.8a15.1 15.1 0 0 0 6.6 6.6l2.2-2.2a1 1 0 0 1 1-.25 11.4 11.4 0 0 0 3.6.57 1 1 0 0 1 1 1V20a1 1 0 0 1-1 1A17 17 0 0 1 3 4a1 1 0 0 1 1-1h3.5a1 1 0 0 1 1 1c0 1.25.2 2.45.57 3.57a1 1 0 0 1-.25 1z"/></svg>
        (662) 555-0147
      </li>
      <li>
        <svg viewBox="0 0 24 24" aria-hidden="true"><path d="M2 5h20v14H2z M3.5 6.5 12 13l8.5-6.5v-.2h-17z" fill-rule="evenodd"/></svg>
        info@harborlinesignal.com
      </li>
      <li>
        <svg viewBox="0 0 24 24" aria-hidden="true"><path d="M12 2a10 10 0 1 0 0 20 10 10 0 0 0 0-20zm6.9 6h-3a15 15 0 0 0-1.3-4 8 8 0 0 1 4.3 4zM12 4c.8 1.1 1.5 2.5 1.9 4h-3.8c.4-1.5 1.1-2.9 1.9-4zM4.3 14a8 8 0 0 1 0-4h3.4a16 16 0 0 0 0 4zm.8 2h3a15 15 0 0 0 1.3 4 8 8 0 0 1-4.3-4zm3-8h-3a8 8 0 0 1 4.3-4 15 15 0 0 0-1.3 4zM12 20c-.8-1.1-1.5-2.5-1.9-4h3.8c-.4 1.5-1.1 2.9-1.9 4zm2.3-6H9.7a14 14 0 0 1 0-4h4.6a14 14 0 0 1 0 4zm.3 6a15 15 0 0 0 1.3-4h3a8 8 0 0 1-4.3 4zm1.7-6a16 16 0 0 0 0-4h3.4a8 8 0 0 1 0 4z"/></svg>
        www.harborlinesignal.com
      </li>
    </ul>
  </div>

  <div class="address">
    <svg viewBox="0 0 12 16" aria-hidden="true"><path d="M6 0a6 6 0 0 0-6 6c0 4.5 6 10 6 10s6-5.5 6-10a6 6 0 0 0-6-6zm0 8.2A2.2 2.2 0 1 1 6 3.8a2.2 2.2 0 0 1 0 4.4z"/></svg>
    30412 HWY 45 N Amory, MS 38821
  </div>
</section>

</body>
</html>
```